Dalton Power Supply, Inc. Business Card Design

We are an Electrical Distributor looking for a Modern, Professional Business Card design.

Target Market(s)

Residential Commercial Industrial

Industry/Entity Type

Electrical

Contact Information for Business Card

Dalton Power Supply, Inc.
418 Maple Ridge Lane
Brookvale, NC 27514
555-214-7630
555-214-8842 Fax
daltonpower@brightmail-example.net

```html
<!DOCTYPE html>
<html lang="en">
<head>
<meta charset="utf-8">
<title>Dalton Power Supply, Inc. – Business Card</title>
<link rel="stylesheet" href="https://fonts.googleapis.com/css2?family=Montserrat:wght@400;700;800&display=swap">
<style>
  :root {
    --page-bg: #e9e7e3;
    --navy: #2a2fa8;
    --navy-deep: #1f2390;
    --cyan: #27b6e8;
    --cyan-soft: #4cc8f0;
    --white: #ffffff;
    --ink-navy: #24288f;
  }
  html, body {
    margin: 0;
    width: 1200px;
    height: 1022px;
    overflow: hidden;
    background: var(--page-bg);
    font-family: "Montserrat", Arial, sans-serif;
  }
  .card {
    position: absolute;
    left: 250px;
    top: 311px;
    width: 700px;
    height: 400px;
    border-radius: 18px;
    overflow: hidden;
    background: linear-gradient(160deg, var(--navy) 0%, var(--navy-deep) 100%);
    box-shadow: 0 10px 30px rgba(0,0,0,0.18);
  }
  .wire-art {
    position: absolute;
    left: 380px;
    top: 0;
    width: 320px;
    height: 150px;
    background: radial-gradient(ellipse at 45% 60%, rgba(120,140,255,0.45), rgba(42,47,168,0) 70%);
  }
  .brand {
    position: absolute;
    left: 44px;
    top: 56px;
    display: flex;
    align-items: center;
    gap: 14px;
  }
  .brand-dot {
    width: 18px;
    height: 18px;
    border-radius: 50%;
    background: var(--cyan-soft);
  }
  .brand-name {
    color: var(--white);
    font-weight: 800;
    font-size: 34px;
    letter-spacing: 0.5px;
  }
  .stripe {
    position: absolute;
    left: 0;
    right: 0;
    height: 3px;
    background: var(--white);
  }
  .stripe-top { top: 150px; }
  .stripe-bottom { top: 297px; }
  .band {
    position: absolute;
    left: 0;
    right: 0;
    top: 164px;
    height: 112px;
    background: var(--cyan);
    border-top: 4px solid var(--white);
    border-bottom: 4px solid var(--white);
  }
  .contact {
    position: absolute;
    left: 44px;
    top: 17px;
    color: var(--white);
    font-size: 16px;
    line-height: 26px;
  }
  .contact-row { display: flex; align-items: center; gap: 10px; }
  .contact-row svg { width: 15px; height: 15px; flex: none; }
  .person {
    position: absolute;
    left: 430px;
    top: 26px;
    color: var(--ink-navy);
  }
  .person-name { font-weight: 800; font-size: 30px; letter-spacing: 1px; line-height: 36px; }
  .person-title { font-size: 15px; letter-spacing: 1px; margin-top: 4px; }
  .address {
    position: absolute;
    left: 430px;
    top: 322px;
    color: var(--white);
    font-size: 16px;
    line-height: 24px;
  }
</style>
</head>
<body>
  <div class="card">
    <div class="wire-art" role="img" aria-label="Glowing electrical wires with sparks"></div>
    <div class="brand">
      <span class="brand-dot"></span>
      <span class="brand-name">DALTON POWER SUPPLY, INC.</span>
    </div>
    <div class="stripe stripe-top"></div>
    <div class="band">
      <div class="contact">
        <div class="contact-row">
          <svg viewBox="0 0 16 16" aria-hidden="true"><path fill="#fff" d="M3 1l3 3-2 2c1 2 3 4 5 5l2-2 3 3-2 3C7 15 1 9 1 3z"/></svg>
          <span>555-214-7630</span>
        </div>
        <div class="contact-row">
          <svg viewBox="0 0 16 16" aria-hidden="true"><rect x="2" y="5" width="12" height="8" rx="1" fill="#fff"/><rect x="4" y="1" width="8" height="5" fill="#fff"/></svg>
          <span>555-214-8842</span>
        </div>
        <div class="contact-row">
          <svg viewBox="0 0 16 16" aria-hidden="true"><rect x="1.5" y="3.5" width="13" height="9" fill="none" stroke="#fff" stroke-width="1.5"/><path d="M2 4l6 5 6-5" fill="none" stroke="#fff" stroke-width="1.5"/></svg>
          <span>daltonpower@brightmail-example.net</span>
        </div>
      </div>
      <div class="person">
        <div class="person-name">MARCUS HALE</div>
        <div class="person-title">DIRECTOR</div>
      </div>
    </div>
    <div class="stripe stripe-bottom"></div>
    <div class="address">
      418 Maple Ridge Lane<br>
      Brookvale, NC 27514
    </div>
  </div>
</body>
</html>
```